Consulting Company PowerPoint Template Design

We are looking for an updated PowerPoint template design or our 55 person energy consulting firm (K7) based in San Francisco (www.kayseven.example). We would like two versions of the same PowerPoint template in a 16:9 and 4:3 format with our existing logo.

We have an existing color scheme and template and are seeking your help to polish/update the template design for wide format and create a flexible template that is easy to use with content from Excel and Word. Our current template, and a couple of examples that we like are attached.

Specific requests include:

• Dark background for slide title
• A narrow section header
• Maximizing white space for content
• A limited number of well designed Master template layouts to choose from
• A selection of title and section header slides that are not San Francisco specific with some variety to chose from ideally with a focus on energy or nature, graphics/visuals.

For examples of energy specific templates see:
https://www.brightslidery.example/energy/powerpoint-templates/0.html

Requirements
Must have
• Must use our logo but open to other designs, fonts, and styles for the PowerPoint template.
• Please use our existing color scheme found in the attached Excel file.
• Also we would like the ability to easily copy and paste from our existing/original template to the new template. In other words we would like backward compatibility to apply the new template format to our old PowerPoints that use our existing template.

```html
<!DOCTYPE html>
<html lang="en">
<head>
<meta charset="utf-8">
<title>Halden Grid Advisory Template Deck</title>
<link href="https://fonts.googleapis.com/css2?family=Open+Sans:wght@400;600;700&display=swap" rel="stylesheet">
<style>
:root{
  --navy:#0f4c6e;--navy-dk:#0b3a55;--gold:#b88a17;--gold-dk:#9a7210;
  --red:#b3341f;--green:#2f8a3c;--blue:#1d4f91;--ink:#444;--muted:#8a8a8a;
  --line:#dcdcdc;--footer:#9c9c9c;--page:#ececec;--white:#fff;
  --city:linear-gradient(180deg,#1c4a74 0%,#4f6683 38%,#c08a3a 66%,#22364d 100%);
  --towers-blue:linear-gradient(180deg,#245a7c 0%,#2f6585 55%,#123a55 100%);
  --towers-gold:linear-gradient(180deg,#cf981f 0%,#b48016 55%,#85590c 100%);
  --sunset:linear-gradient(180deg,#3b3550 0%,#c45a1f 52%,#f0a23a 66%,#3a1d10 100%);
  --sky:linear-gradient(180deg,#8fb3d1 0%,#c9dae7 60%,#b59b72 100%);
  --portrait:linear-gradient(160deg,#8a6a5a,#3a2c28);
  --world:radial-gradient(ellipse at 30% 40%,#0f4c6e 0 12%,transparent 13%),radial-gradient(ellipse at 70% 30%,#b88a17 0 14%,transparent 15%),radial-gradient(ellipse at 80% 70%,#1d4f91 0 7%,transparent 8%),linear-gradient(180deg,#d6d6d6,#cfcfcf);
  --usa:radial-gradient(ellipse at 45% 55%,#0f4c6e 0 18%,transparent 19%),radial-gradient(ellipse at 72% 55%,#b88a17 0 12%,transparent 13%),linear-gradient(180deg,#d6d6d6,#cfcfcf);
}
*{box-sizing:border-box}
body{margin:0;width:1200px;height:2712px;overflow:hidden;background:var(--page);font-family:'Open Sans',sans-serif;color:var(--ink)}
.deck{display:grid;grid-template-columns:repeat(3,1fr);grid-template-rows:repeat(12,1fr);gap:6.5px 7px;width:1200px;height:2712px}
.slide{position:relative;overflow:hidden;background:var(--white)}
.slide--navy{background:var(--navy)}
.slide--gold{background:var(--gold)}
.photo{position:absolute;inset:0}
.photo--city{background:var(--city)}
.photo--towers-blue{background:var(--towers-blue)}
.photo--towers-gold{background:var(--towers-gold)}

.brand{display:flex;align-items:center;gap:5px;color:var(--white);font-weight:600;font-size:8px;white-space:nowrap}
.brand-mark{width:18px;height:18px;border-radius:50%;background:var(--white);flex:none}
.brand--navy{color:var(--navy)}
.brand--navy .brand-mark{background:var(--navy)}
.brand--lg{font-size:10px}.brand--lg .brand-mark{width:24px;height:24px}
.brand--sm{font-size:5.5px;gap:3px}.brand--sm .brand-mark{width:10px;height:10px}
.centered{position:absolute;left:50%;top:50%;transform:translate(-50%,-50%)}

.footer{position:absolute;left:0;right:0;bottom:0;height:12px;background:var(--footer);display:flex;align-items:center;justify-content:space-between;padding:0 8px;font-size:4.3px;color:var(--white)}
.footer .brand{font-size:4.5px;gap:3px}
.footer .brand-mark{width:8px;height:8px}

.slide-title{position:absolute;left:12px;top:8px;margin:0;font-size:12.5px;font-weight:400;color:var(--navy)}
.body-text{font-size:4.6px;line-height:1.45;color:var(--muted);margin:0}

.cover-title{position:absolute;left:20px;margin:0;color:var(--white);font-weight:400;line-height:1.08}
.cover-sub{position:absolute;left:20px;color:var(--white);font-size:6.5px}
.cover-name{position:absolute;left:20px;color:var(--white);font-size:8px;font-weight:700}
.cover-date{position:absolute;left:20px;color:var(--white);font-size:6.5px}
.rule{position:absolute;height:1px;background:rgba(255,255,255,.8)}

.agenda{position:absolute;left:50px;top:58px;display:grid;grid-template-columns:160px 120px;row-gap:18px}
.agenda-item{display:flex;align-items:center;gap:8px;font-size:8px;color:var(--navy)}
.agenda-num{width:17px;height:17px;border-radius:50%;background:var(--navy);color:var(--white);display:flex;align-items:center;justify-content:center;font-size:7px}

.bullet-block h3{margin:0 0 2px;font-size:5.8px;font-weight:700;color:#333}
.bullet-block h3::before{content:"■ ";color:var(--navy)}
.bullet-block{margin-bottom:6px}

.avatar{border-radius:50%;border:3px solid var(--white);box-shadow:0 0 0 1px var(--line);background:var(--portrait)}

.data-table{position:absolute;left:40px;top:34px;border-collapse:separate;border-spacing:2px;font-size:5.5px}
.data-table th{background:var(--navy);color:var(--white);font-weight:400;padding:3px 8px}
.data-table td{padding:4px 8px;color:#555;text-align:center;border-bottom:1px solid var(--line)}
.data-table td.row-label{background:var(--navy);color:var(--white);text-align:left;border:none}

.legend{position:absolute;font-size:4.6px;color:var(--muted);display:flex;flex-direction:column;gap:4px}
.legend span{display:flex;align-items:center;gap:4px}
.legend i{width:9px;height:9px;border-radius:50%;display:inline-block}

.map{position:absolute;border-radius:3px}

svg text{font-family:'Open Sans',sans-serif}
.dots{display:flex;gap:3px;justify-content:center}
.dots i{width:5px;height:5px;border-radius:50%;background:var(--navy)}
</style>
</head>
<body>
<main class="deck">

<!-- Row 1 -->
<section class="slide slide--navy">
  <div class="brand brand--lg centered"><span class="brand-mark"></span>Halden Grid Advisory</div>
</section>

<section class="slide">
  <div class="photo photo--city" role="img" aria-label="City skyline at dusk with bay and lit avenue"></div>
  <div style="position:absolute;left:0;right:0;top:70px;height:48px;background:rgba(255,255,255,.85)"></div>
  <div class="brand brand--navy brand--lg" style="position:absolute;left:36px;top:82px"><span class="brand-mark"></span>Halden Grid Advisory</div>
  <footer class="footer"><span class="brand"><span class="brand-mark"></span>Halden Grid Advisory</span><span>© 2017 Halden Grid Advisory. All rights reserved.</span><span>Page | 2</span></footer>
</section>

<section class="slide">
  <div class="photo photo--towers-blue" style="bottom:auto;height:100px" role="img" aria-label="Power transmission towers at dusk"></div>
  <div style="position:absolute;left:0;right:0;top:12px;text-align:center;color:#fff;font-size:13px;font-weight:700">Presentation Title</div>
  <div style="position:absolute;left:0;right:0;top:30px;text-align:center;color:var(--gold);font-size:9px;font-weight:700">Presented By</div>
  <div class="avatar" style="position:absolute;left:170px;top:48px;width:58px;height:58px" role="img" aria-label="Portrait of the presenter"></div>
  <div style="position:absolute;left:0;right:0;top:114px;text-align:center;color:var(--navy);font-size:8.5px;font-weight:700">Alex Moran</div>
  <div style="position:absolute;left:0;right:0;top:127px;text-align:center;color:var(--gold);font-size:5.5px">President CEO</div>
  <footer class="footer"><span class="brand"><span class="brand-mark"></span>Halden Grid Advisory</span><span>© 2017 Halden Grid Advisory. All rights reserved.</span><span>Page | 3</span></footer>
</section>

<!-- Row 2 -->
<section class="slide">
  <div class="photo photo--towers-blue" role="img" aria-label="Aerial city view at night in blue tint"></div>
  <div class="brand brand--lg centered"><span class="brand-mark"></span>Halden Grid Advisory</div>
</section>

<section class="slide slide--gold">
  <div class="brand brand--lg centered"><span class="brand-mark"></span>Halden Grid Advisory</div>
</section>

<section class="slide">
  <div class="photo photo--towers-gold" role="img" aria-label="Transmission towers in golden haze"></div>
  <div class="brand brand--lg centered"><span class="brand-mark"></span>Halden Grid Advisory</div>
</section>

<!-- Row 3 -->
<section class="slide slide--navy">
  <h1 class="cover-title" style="top:60px;font-size:22px">TITLE OF THE<br>PRESENTATION</h1>
  <div class="rule" style="left:20px;top:113px;width:180px"></div>
  <div class="cover-sub" style="top:118px">Your Subtitle Goes Here</div>
  <div class="brand" style="position:absolute;left:210px;top:104px"><span class="brand-mark"></span>Halden Grid Advisory</div>
  <div class="cover-name" style="top:168px">Jane Smith, Public Analyst</div>
  <div class="cover-date" style="top:180px">June 24, 2017</div>
</section>

<section class="slide slide--gold">
  <h1 class="cover-title" style="top:60px;font-size:22px">TITLE OF THE<br>PRESENTATION</h1>
  <div class="rule" style="left:20px;top:113px;width:180px"></div>
  <div class="cover-sub" style="top:118px">Your Subtitle Goes Here</div>
  <div class="brand" style="position:absolute;left:210px;top:104px"><span class="brand-mark"></span>Halden Grid Advisory</div>
  <div class="cover-name" style="top:168px">Jane Smith, Public Analyst</div>
  <div class="cover-date" style="top:180px">June 24, 2017</div>
</section>

<section class="slide">
  <div class="photo photo--towers-blue" role="img" aria-label="Sunset over power lines in blue tint"></div>
  <div class="brand brand--sm" style="position:absolute;left:20px;top:20px"><span class="brand-mark"></span>Halden Grid Advisory</div>
  <h1 class="cover-title" style="top:78px;font-size:20px">YOUR PRESENTATION<br>TITLE GOES HERE</h1>
  <div class="cover-sub" style="top:122px">Your Subtitle Goes Here</div>
  <div class="cover-name" style="top:180px">Jane Smith, Public Analyst</div>
</section>

<!-- Row 4 -->
<section class="slide">
  <div class="photo photo--towers-blue" role="img" aria-label="Transmission towers under sky in blue tint"></div>
  <div class="brand brand--sm" style="position:absolute;left:20px;top:20px"><span class="brand-mark"></span>Halden Grid Advisory</div>
  <h1 class="cover-title" style="top:78px;font-size:20px">YOUR PRESENTATION<br>TITLE GOES HERE</h1>
  <div class="cover-sub" style="top:122px">Your Subtitle Goes Here</div>
  <div class="cover-name" style="top:180px">Jane Smith, Public Analyst</div>
</section>

<section class="slide">
  <div class="photo photo--towers-gold" role="img" aria-label="Transmission towers at sunset in gold tint"></div>
  <div class="brand brand--sm" style="position:absolute;left:20px;top:20px"><span class="brand-mark"></span>Halden Grid Advisory</div>
  <h1 class="cover-title" style="top:78px;font-size:20px">YOUR PRESENTATION<br>TITLE GOES HERE</h1>
  <div class="cover-sub" style="top:122px">Your Subtitle Goes Here</div>
  <div class="cover-name" style="top:180px">Jane Smith, Public Analyst</div>
</section>

<section class="slide">
  <h2 class="slide-title">Our Agenda</h2>
  <div class="agenda">
    <div class="agenda-item"><span class="agenda-num">1</span>Agenda One</div>
    <div class="agenda-item"><span class="agenda-num">4</span>Agenda Four</div>
    <div class="agenda-item"><span class="agenda-num">2</span>Agenda Two</div>
    <div class="agenda-item"><span class="agenda-num">5</span>Agenda Five</div>
    <div class="agenda-item"><span class="agenda-num">3</span>Agenda Three</div>
    <div class="agenda-item"><span class="agenda-num">6</span>Agenda Six</div>
  </div>
  <footer class="footer"><span class="brand"><span class="brand-mark"></span>Halden Grid Advisory</span><span>© 2017 Halden Grid Advisory. All rights reserved.</span><span>Page | 12</span></footer>
</section>

<!-- Row 5 -->
<section class="slide">
  <h2 class="slide-title">Welcome Message</h2>
  <div class="avatar" style="position:absolute;left:160px;top:30px;width:72px;height:72px" role="img" aria-label="Portrait of the company leader"></div>
  <div style="position:absolute;left:0;right:0;top:108px;text-align:center;font-size:5.5px;color:#555">Jo Anderson<br>CEO</div>
  <p class="body-text" style="position:absolute;left:120px;width:155px;top:126px;text-align:center">Lorem ipsum dolor sit amet, consectetur adipiscing elit, sed do eiusmod tempor incididunt ut labore et dolore magna aliqua. Ut enim ad minim veniam, quis nostrud.</p>
  <div class="dots" style="position:absolute;left:0;right:0;top:165px"><i></i><i></i><i></i><i></i></div>
  <footer class="footer"><span class="brand"><span class="brand-mark"></span>Halden Grid Advisory</span><span>© 2017 Halden Grid Advisory. All rights reserved.</span><span>Page | 13</span></footer>
</section>

<section class="slide">
  <h2 class="slide-title">One Column Bullets List</h2>
  <div style="position:absolute;left:14px;right:14px;top:32px">
    <div class="bullet-block"><h3>The standard lorem ipsum passage, used since the 1500s</h3><p class="body-text">Lorem ipsum dolor sit amet, consectetur adipiscing elit, sed do eiusmod tempor incididunt ut labore et dolore magna aliqua. Ut enim ad minim veniam, quis nostrud exercitation ullamco laboris nisi ut aliquip ex ea commodo consequat. Duis aute irure dolor in reprehenderit in voluptate velit esse cillum dolore eu fugiat nulla pariatur.</p></div>
    <div class="bullet-block"><h3>The standard lorem ipsum passage, used since the 1500s</h3><p class="body-text">Lorem ipsum dolor sit amet, consectetur adipiscing elit, sed do eiusmod tempor incididunt ut labore et dolore magna aliqua. Ut enim ad minim veniam, quis nostrud exercitation ullamco laboris nisi ut aliquip ex ea commodo consequat. Duis aute irure dolor in reprehenderit in voluptate velit esse cillum dolore eu fugiat nulla pariatur.</p></div>
    <div class="bullet-block"><h3>The standard lorem ipsum passage, used since the 1500s</h3><p class="body-text">Lorem ipsum dolor sit amet, consectetur adipiscing elit, sed do eiusmod tempor incididunt ut labore et dolore magna aliqua. Ut enim ad minim veniam, quis nostrud exercitation ullamco laboris nisi ut aliquip ex ea commodo consequat.</p></div>
  </div>
  <footer class="footer"><span class="brand"><span class="brand-mark"></span>Halden Grid Advisory</span><span>© 2017 Halden Grid Advisory. All rights reserved.</span><span>Page | 14</span></footer>
</section>

<section class="slide">
  <h2 class="slide-title">Two Column Bullets List</h2>
  <div style="position:absolute;left:14px;right:14px;top:32px;display:grid;grid-template-columns:1fr 1fr;column-gap:14px">
    <div class="bullet-block"><h3>The standard lorem ipsum passage, used since</h3><p class="body-text">Lorem ipsum dolor sit amet, consectetur adipiscing elit, sed do eiusmod tempor incididunt ut labore et dolore magna aliqua. Ut enim ad minim veniam, quis nostrud exercitation ullamco laboris nisi ut aliquip ex ea commodo.</p></div>
    <div class="bullet-block"><h3>The standard lorem ipsum passage, used since</h3><p class="body-text">Lorem ipsum dolor sit amet, consectetur adipiscing elit, sed do eiusmod tempor incididunt ut labore et dolore magna aliqua. Ut enim ad minim veniam, quis nostrud exercitation ullamco laboris nisi ut aliquip ex ea commodo.</p></div>
    <div class="bullet-block"><h3>The standard lorem ipsum passage, used since</h3><p class="body-text">Lorem ipsum dolor sit amet, consectetur adipiscing elit, sed do eiusmod tempor incididunt ut labore et dolore magna aliqua. Ut enim ad minim veniam, quis nostrud exercitation ullamco laboris nisi ut aliquip ex ea commodo.</p></div>
    <div class="bullet-block"><h3>The standard lorem ipsum passage, used since</h3><p class="body-text">Lorem ipsum dolor sit amet, consectetur adipiscing elit, sed do eiusmod tempor incididunt ut labore et dolore magna aliqua. Ut enim ad minim veniam, quis nostrud exercitation ullamco laboris nisi ut aliquip ex ea commodo.</p></div>
  </div>
  <footer class="footer"><span class="brand"><span class="brand-mark"></span>Halden Grid Advisory</span><span>© 2017 Halden Grid Advisory. All rights reserved.</span><span>Page | 15</span></footer>
</section>

<!-- Row 6 -->
<section class="slide">
  <h2 class="slide-title">Three Column And Text</h2>
  <div style="position:absolute;left:14px;top:34px;width:112px;height:72px;background:var(--sunset)" role="img" aria-label="Power lines against orange sunset"></div>
  <div style="position:absolute;left:142px;top:34px;width:112px;height:72px;background:var(--towers-blue)" role="img" aria-label="Transmission tower in blue tint with caption"></div>
  <div style="position:absolute;left:270px;top:34px;width:112px;height:72px;background:linear-gradient(180deg,#3b4f8a,#8a7fb5 55%,#d9b88a)" role="img" aria-label="Towers under violet evening sky"></div>
  <p class="body-text" style="position:absolute;left:14px;top:118px;width:112px">Lorem ipsum dolor sit amet, consectetur adipiscing elit, sed do eiusmod tempor incididunt ut labore et dolore magna aliqua ut enim.</p>
  <p class="body-text" style="position:absolute;left:142px;top:118px;width:112px">Lorem ipsum dolor sit amet, consectetur adipiscing elit, sed do eiusmod tempor incididunt ut labore et dolore magna aliqua ut enim.</p>
  <p class="body-text" style="position:absolute;left:270px;top:118px;width:112px">Lorem ipsum dolor sit amet, consectetur adipiscing elit, sed do eiusmod tempor incididunt ut labore et dolore magna aliqua ut enim.</p>
  <footer class="footer"><span class="brand"><span class="brand-mark"></span>Halden Grid Advisory</span><span>© 2017 Halden Grid Advisory. All rights reserved.</span><span>Page | 16</span></footer>
</section>

<section class="slide slide--navy">
  <div class="brand brand--sm" style="position:absolute;left:90px;top:80px"><span class="brand-mark"></span>Halden Grid Advisory</div>
  <div class="rule" style="left:20px;top:100px;width:185px"></div>
  <h2 style="position:absolute;left:20px;top:114px;margin:0;color:#fff;font-size:15px;font-weight:400">YOUR DIVIDER PAGE</h2>
</section>

<section class="slide slide--gold">
  <div class="brand brand--sm" style="position:absolute;left:90px;top:80px"><span class="brand-mark"></span>Halden Grid Advisory</div>
  <div class="rule" style="left:20px;top:100px;width:185px"></div>
  <h2 style="position:absolute;left:20px;top:114px;margin:0;color:#fff;font-size:15px;font-weight:400">YOUR DIVIDER PAGE</h2>
</section>

<!-- Row 7 -->
<section class="slide">
  <h2 class="slide-title">Graphic Chart</h2>
  <svg style="position:absolute;left:0;top:0" width="395" height="208" viewBox="0 0 395 208">
    <g font-size="4.5" fill="#888">
      <rect x="145" y="27" width="5" height="5" fill="var(--navy)"/><text x="152" y="31">Series 1</text>
      <rect x="180" y="27" width="5" height="5" fill="var(--gold)"/><text x="187" y="31">Series 2</text>
      <rect x="215" y="27" width="5" height="5" fill="var(--red)"/><text x="222" y="31">Series 3</text>
      <text x="14" y="52">Category 1</text><text x="14" y="79">Category 2</text><text x="14" y="106">Category 3</text><text x="14" y="133">Category 4</text>
    </g>
    <line x1="50" y1="38" x2="50" y2="142" stroke="#ddd"/>
    <g>
      <rect x="50" y="45" width="70" height="10" fill="var(--navy)"/><rect x="120" y="45" width="55" height="10" fill="var(--gold)"/><rect x="175" y="45" width="95" height="10" fill="var(--red)"/>
      <rect x="50" y="72" width="45" height="10" fill="var(--navy)"/><rect x="95" y="72" width="50" height="10" fill="var(--gold)"/><rect x="145" y="72" width="55" height="10" fill="var(--red)"/>
      <rect x="50" y="99" width="100" height="10" fill="var(--navy)"/><rect x="150" y="99" width="40" height="10" fill="var(--gold)"/><rect x="190" y="99" width="80" height="10" fill="var(--red)"/>
      <rect x="50" y="126" width="60" height="10" fill="var(--navy)"/><rect x="110" y="126" width="45" height="10" fill="var(--gold)"/><rect x="155" y="126" width="50" height="10" fill="var(--red)"/>
    </g>
  </svg>
  <p class="body-text" style="position:absolute;left:14px;right:14px;top:158px">Lorem ipsum dolor sit amet, consectetur adipiscing elit, sed do eiusmod tempor incididunt ut labore et dolore magna aliqua. Ut enim ad minim veniam, quis nostrud exercitation ullamco laboris nisi ut aliquip ex ea commodo.</p>
  <footer class="footer"><span class="brand"><span class="brand-mark"></span>Halden Grid Advisory</span><span>© 2017 Halden Grid Advisory. All rights reserved.</span><span>Page | 17</span></footer>
</section>

<section class="slide">
  <h2 class="slide-title">Our Chart</h2>
  <svg style="position:absolute;left:0;top:0" width="395" height="208" viewBox="0 0 395 208">
    <g fill="var(--navy)"><rect x="60" y="30" width="10" height="3"/><rect x="90" y="30" width="10" height="3" fill="var(--gold)"/><rect x="120" y="30" width="10" height="3" fill="var(--red)"/><rect x="150" y="30" width="10" height="3" fill="var(--green)"/><rect x="180" y="30" width="10" height="3"/><rect x="210" y="30" width="10" height="3" fill="var(--gold)"/><rect x="240" y="30" width="10" height="3" fill="var(--red)"/><rect x="270" y="30" width="10" height="3" fill="var(--green)"/><rect x="300" y="30" width="10" height="3"/></g>
    <path d="M40 90 C70 40,100 40,120 90 S170 150,200 110 S250 60,280 110 S330 150,360 110" fill="none" stroke="var(--navy)" stroke-width="2.5"/>
    <path d="M280 110 C300 140,330 150,360 110" fill="none" stroke="var(--gold)" stroke-width="2.5" stroke-dasharray="2 3"/>
    <line x1="30" y1="150" x2="370" y2="150" stroke="#ddd"/>
  </svg>
  <p class="body-text" style="position:absolute;left:14px;right:14px;top:170px">Lorem ipsum dolor sit amet, consectetur adipiscing elit, sed do eiusmod tempor incididunt ut labore et dolore magna aliqua. Ut enim ad minim veniam, quis nostrud exercitation.</p>
  <footer class="footer"><span class="brand"><span class="brand-mark"></span>Halden Grid Advisory</span><span>© 2017 Halden Grid Advisory. All rights reserved.</span><span>Page | 18</span></footer>
</section>

<section class="slide">
  <h2 class="slide-title">Image + Text</h2>
  <div style="position:absolute;left:14px;top:45px;width:190px;height:120px;background:var(--sunset)" role="img" aria-label="Transmission tower silhouetted at sunset"></div>
  <div style="position:absolute;left:218px;top:50px;right:14px">
    <div class="bullet-block"><h3 style="color:var(--gold)">Lorem ipsum dolor sit amet</h3><p class="body-text">Consectetur adipiscing elit, sed do eiusmod tempor incididunt ut labore et dolore magna.</p></div>
    <div class="bullet-block"><h3 style="color:var(--gold)">Lorem ipsum dolor sit amet</h3><p class="body-text">Consectetur adipiscing elit, sed do eiusmod tempor incididunt ut labore et dolore magna.</p></div>
    <div class="bullet-block"><h3 style="color:var(--gold)">Lorem ipsum dolor sit amet</h3><p class="body-text">Consectetur adipiscing elit, sed do eiusmod tempor incididunt ut labore et dolore magna.</p></div>
  </div>
  <footer class="footer"><span class="brand"><span class="brand-mark"></span>Halden Grid Advisory</span><span>© 2017 Halden Grid Advisory. All rights reserved.</span><span>Page | 19</span></footer>
</section>

<!-- Row 8 -->
<section class="slide">
  <h2 class="slide-title">Line Chart</h2>
  <svg style="position:absolute;left:0;top:0" width="395" height="208" viewBox="0 0 395 208">
    <g stroke="#e6e6e6"><line x1="40" y1="40" x2="370" y2="40"/><line x1="40" y1="65" x2="370" y2="65"/><line x1="40" y1="90" x2="370" y2="90"/><line x1="40" y1="115" x2="370" y2="115"/><line x1="40" y1="140" x2="370" y2="140"/><line x1="40" y1="165" x2="370" y2="165"/></g>
    <g font-size="4.5" fill="#999"><text x="30" y="42">6</text><text x="30" y="67">5</text><text x="30" y="92">4</text><text x="30" y="117">3</text><text x="30" y="142">2</text><text x="30" y="167">1</text>
      <text x="62" y="176">Category 1</text><text x="142" y="176">Category 2</text><text x="222" y="176">Category 3</text><text x="302" y="176">Category 4</text></g>
    <polyline points="75,40 155,125 235,80 335,60" fill="none" stroke="var(--navy)" stroke-width="2"/>
    <polyline points="75,125 155,60 235,120 335,90" fill="none" stroke="var(--gold)" stroke-width="2"/>
    <g fill="#fff" stroke-width="2"><circle cx="75" cy="40" r="3" stroke="var(--navy)"/><circle cx="155" cy="125" r="3" stroke="var(--navy)"/><circle cx="235" cy="80" r="3" stroke="var(--navy)"/><circle cx="335" cy="60" r="3" stroke="var(--navy)"/>
      <circle cx="75" cy="125" r="3" stroke="var(--gold)"/><circle cx="155" cy="60" r="3" stroke="var(--gold)"/><circle cx="235" cy="120" r="3" stroke="var(--gold)"/><circle cx="335" cy="90" r="3" stroke="var(--gold)"/></g>
    <rect x="220" y="62" width="42" height="11" rx="5.5" fill="var(--navy)"/><text x="226" y="69.5" font-size="4.5" fill="#fff">Lorem ipsum</text>
    <rect x="100" y="130" width="42" height="11" rx="5.5" fill="var(--gold)"/><text x="106" y="137.5" font-size="4.5" fill="#fff">Lorem ipsum</text>
  </svg>
  <p class="body-text" style="position:absolute;left:14px;right:14px;top:184px">Lorem ipsum dolor sit amet, consectetur adipiscing elit, sed do eiusmod tempor incididunt ut labore et dolore magna aliqua ut enim ad minim.</p>
  <footer class="footer"><span class="brand"><span class="brand-mark"></span>Halden Grid Advisory</span><span>© 2017 Halden Grid Advisory. All rights reserved.</span><span>Page | 20</span></footer>
</section>

<section class="slide">
  <div style="position:absolute;left:14px;top:6px;font-size:4.5px;color:var(--muted)">Lorem ipsum dolor sit</div>
  <h2 class="slide-title" style="top:12px;font-size:9px;color:#333">• TWO IMAGES + BULLETS TEXT</h2>
  <div style="position:absolute;left:14px;top:40px;width:175px;height:78px;background:var(--sunset)" role="img" aria-label="Power lines at sunset"></div>
  <div style="position:absolute;left:206px;top:40px;width:175px;height:78px;background:var(--sky)" role="img" aria-label="Wind turbines on open land"></div>
  <div style="position:absolute;left:14px;top:112px;width:175px;height:8px;background:var(--navy);color:#fff;font-size:4.3px;text-align:center;line-height:8px">Lorem ipsum dolor sit amet</div>
  <div style="position:absolute;left:206px;top:112px;width:175px;height:8px;background:var(--navy);color:#fff;font-size:4.3px;text-align:center;line-height:8px">Lorem ipsum dolor sit amet</div>
  <p class="body-text" style="position:absolute;left:14px;top:128px;width:175px">• Lorem ipsum dolor sit amet, consectetur adipiscing elit sed do eiusmod.<br>• Tempor incididunt ut labore et dolore magna aliqua ut enim ad minim.<br>• Quis nostrud exercitation ullamco laboris nisi ut aliquip ex ea.</p>
  <p class="body-text" style="position:absolute;left:206px;top:128px;width:175px">• Lorem ipsum dolor sit amet, consectetur adipiscing elit sed do eiusmod.<br>• Tempor incididunt ut labore et dolore magna aliqua ut enim ad minim.<br>• Quis nostrud exercitation ullamco laboris nisi ut aliquip ex ea.</p>
  <footer class="footer"><span class="brand"><span class="brand-mark"></span>Halden Grid Advisory</span><span>© 2017 Halden Grid Advisory. All rights reserved.</span><span>Page | 21</span></footer>
</section>

<section class="slide">
  <h2 class="slide-title">Editable World Map</h2>
  <div class="map" style="left:75px;top:30px;width:305px;height:140px;background:var(--world)" role="img" aria-label="World map with highlighted countries in navy, gold, red and blue"></div>
  <div class="legend" style="left:14px;top:128px">
    <span><i style="background:var(--navy)"></i>Lorem ipsum dolor sit</span>
    <span><i style="background:var(--gold)"></i>Lorem ipsum dolor sit</span>
    <span><i style="background:var(--blue)"></i>Lorem ipsum dolor sit</span>
    <span><i style="background:var(--red)"></i>Lorem ipsum dolor sit</span>
  </div>
  <footer class="footer"><span class="brand"><span class="brand-mark"></span>Halden Grid Advisory</span><span>© 2017 Halden Grid Advisory. All rights reserved.</span><span>Page | 22</span></footer>
</section>

<!-- Row 9 -->
<section class="slide">
  <h2 class="slide-title">Our Table Area</h2>
  <table class="data-table">
    <tr><th></th><th>Column 1</th><th>Column 2</th><th>Column 3</th><th>Column 4</th><th>Column 5</th><th>Column 6</th></tr>
    <tr><td class="row-label">Row Sample #1</td><td>21</td><td>36</td><td>31</td><td>23</td><td>80</td><td>57</td></tr>
    <tr><td class="row-label">Row Sample #2</td><td>81</td><td>56</td><td>29</td><td>19</td><td>65</td><td>32</td></tr>
    <tr><td class="row-label">Row Sample #3</td><td>50</td><td>42</td><td>71</td><td>57</td><td>93</td><td>64</td></tr>
    <tr><td class="row-label">Row Sample #4</td><td>74</td><td>28</td><td>43</td><td>41</td><td>27</td><td>39</td></tr>
    <tr><td class="row-label">Row Sample #5</td><td>22</td><td>74</td><td>14</td><td>98</td><td>72</td><td>97</td></tr>
  </table>
  <footer class="footer"><span class="brand"><span class="brand-mark"></span>Halden Grid Advisory</span><span>© 2017 Halden Grid Advisory. All rights reserved.</span><span>Page | 23</span></footer>
</section>

<section class="slide">
  <h2 class="slide-title">Three Column Chart</h2>
  <svg style="position:absolute;left:0;top:0" width="395" height="208" viewBox="0 0 395 208">
    <defs>
      <g id="pie">
        <path d="M20 20 L20 2 A18 18 0 1 1 14.44 37.12 Z" fill="var(--navy)"/>
        <path d="M20 20 L14.44 37.12 A18 18 0 0 1 2.88 14.44 Z" fill="var(--gold)"/>
        <path d="M20 20 L2.88 14.44 A18 18 0 0 1 20 2 Z" fill="var(--green)"/>
      </g>
    </defs>
    <g font-size="4.5" fill="#fff">
      <rect x="45" y="32" width="40" height="9" rx="4.5" fill="var(--navy)"/><text x="50" y="38.5">Heading Text</text>
      <rect x="177" y="32" width="40" height="9" rx="4.5" fill="var(--navy)"/><text x="182" y="38.5">Heading Text</text>
      <rect x="309" y="32" width="40" height="9" rx="4.5" fill="var(--navy)"/><text x="314" y="38.5">Heading Text</text>
    </g>
    <use href="#pie" transform="translate(33 44) scale(1.6)"/>
    <use href="#pie" transform="translate(165 44) scale(1.6)"/>
    <use href="#pie" transform="translate(297 44) scale(1.6)"/>
  </svg>
  <p class="body-text" style="position:absolute;left:25px;top:118px;width:92px">Lorem ipsum dolor sit amet, consectetur adipiscing elit, sed do eiusmod tempor incididunt ut labore et dolore magna aliqua.</p>
  <p class="body-text" style="position:absolute;left:155px;top:118px;width:92px">Lorem ipsum dolor sit amet, consectetur adipiscing elit, sed do eiusmod tempor incididunt ut labore et dolore magna aliqua.</p>
  <p class="body-text" style="position:absolute;left:285px;top:118px;width:92px">Lorem ipsum dolor sit amet, consectetur adipiscing elit, sed do eiusmod tempor incididunt ut labore et dolore magna aliqua.</p>
  <footer class="footer"><span class="brand"><span class="brand-mark"></span>Halden Grid Advisory</span><span>© 2017 Halden Grid Advisory. All rights reserved.</span><span>Page | 24</span></footer>
</section>

<section class="slide">
  <h2 class="slide-title">Editable U.S Map</h2>
  <div class="map" style="left:120px;top:28px;width:262px;height:150px;background:var(--usa)" role="img" aria-label="United States map with states highlighted in navy, gold, red and green"></div>
  <div class="legend" style="left:14px;top:105px">
    <span><i style="background:var(--navy)"></i>Lorem ipsum dolor sit</span>
    <span><i style="background:var(--gold)"></i>Lorem ipsum dolor sit</span>
    <span><i style="background:var(--navy-dk)"></i>Lorem ipsum dolor sit</span>
    <span><i style="background:var(--green)"></i>Lorem ipsum dolor sit</span>
    <span><i style="background:var(--red)"></i>Lorem ipsum dolor sit</span>
  </div>
  <footer class="footer"><span class="brand"><span class="brand-mark"></span>Halden Grid Advisory</span><span>© 2017 Halden Grid Advisory. All rights reserved.</span><span>Page | 25</span></footer>
</section>

<!-- Row 10 -->
<section class="slide">
  <h2 class="slide-title">Project Timeline #1</h2>
  <svg style="position:absolute;left:0;top:0" width="395" height="208" viewBox="0 0 395 208">
    <rect x="90" y="60" width="90" height="4" fill="var(--navy)"/>
    <rect x="150" y="75" width="130" height="4" fill="var(--gold)"/>
    <rect x="150" y="87" width="155" height="4" fill="var(--navy)"/>
    <rect x="200" y="99" width="110" height="4" fill="var(--gold)"/>
    <rect x="125" y="111" width="120" height="4" fill="var(--navy)"/>
    <g font-size="4" fill="#888"><text x="90" y="55">Lorem ipsum dolor sit amet</text><text x="230" y="52">Lorem ipsum dolor sit amet</text><text x="230" y="58">consectetur adipiscing</text></g>
    <line x1="70" y1="145" x2="330" y2="145" stroke="#ccc"/>
    <g fill="var(--navy)"><circle cx="90" cy="145" r="2"/><circle cx="138" cy="145" r="2"/><circle cx="186" cy="145" r="2"/><circle cx="234" cy="145" r="2"/><circle cx="282" cy="145" r="2"/><circle cx="325" cy="145" r="2"/></g>
    <g font-size="4.5" fill="var(--navy)" text-anchor="middle"><text x="90" y="156">January</text><text x="138" y="156">February</text><text x="186" y="156">March</text><text x="234" y="156">April</text><text x="282" y="156">May</text><text x="325" y="156">June</text></g>
  </svg>
  <footer class="footer"><span class="brand"><span class="brand-mark"></span>Halden Grid Advisory</span><span>© 2017 Halden Grid Advisory. All rights reserved.</span><span>Page | 26</span></footer>
</section>

<section class="slide">
  <h2 class="slide-title">Project Timeline #2</h2>
  <svg style="position:absolute;left:0;top:0" width="395" height="208" viewBox="0 0 395 208">
    <rect x="110" y="42" width="90" height="6" fill="var(--gold)"/>
    <rect x="25" y="52" width="80" height="6" fill="var(--navy)"/>
    <rect x="120" y="62" width="60" height="6" fill="var(--gold)"/>
    <rect x="215" y="52" width="90" height="6" fill="var(--red)"/>
    <rect x="220" y="66" width="60" height="6" fill="var(--red)"/>
    <g font-size="4.5" fill="#fff" text-anchor="middle">
      <rect x="25" y="82" width="34" height="12" fill="var(--navy)"/><text x="42" y="90">2010</text>
      <rect x="61" y="82" width="34" height="12" fill="var(--navy)"/><text x="78" y="90">2011</text>
      <rect x="97" y="82" width="34" height="12" fill="var(--navy)"/><text x="114" y="90">2012</text>
      <rect x="133" y="82" width="34" height="12" fill="var(--gold)"/><text x="150" y="90">2013</text>
      <rect x="169" y="82" width="34" height="12" fill="var(--gold)"/><text x="186" y="90">2014</text>
      <rect x="205" y="82" width="34" height="12" fill="var(--gold)"/><text x="222" y="90">2015</text>
      <rect x="241" y="82" width="34" height="12" fill="var(--red)"/><text x="258" y="90">2016</text>
      <rect x="277" y="82" width="34" height="12" fill="var(--red)"/><text x="294" y="90">2017</text>
      <rect x="313" y="82" width="34" height="12" fill="var(--red)"/><text x="330" y="90">2018</text>
    </g>
  </svg>
  <p class="body-text" style="position:absolute;left:25px;right:25px;top:140px">Lorem ipsum dolor sit amet, consectetur adipiscing elit, sed do eiusmod tempor incididunt ut labore et dolore magna aliqua. Ut enim ad minim veniam, quis nostrud exercitation ullamco laboris nisi ut aliquip ex ea commodo consequat duis aute.</p>
  <footer class="footer"><span class="brand"><span class="brand-mark"></span>Halden Grid Advisory</span><span>© 2017 Halden Grid Advisory. All rights reserved.</span><span>Page | 27</span></footer>
</section>

<section class="slide">
  <h2 class="slide-title">Our Timeline</h2>
  <svg style="position:absolute;left:0;top:0" width="395" height="208" viewBox="0 0 395 208">
    <line x1="40" y1="78" x2="355" y2="78" stroke="#ccc"/>
    <line x1="80" y1="78" x2="80" y2="108" stroke="#ccc"/>
    <line x1="80" y1="108" x2="330" y2="108" stroke="#ccc"/>
    <g font-size="4.5" fill="#fff" text-anchor="middle">
      <rect x="40" y="50" width="44" height="14" rx="2" fill="var(--navy)"/><text x="62" y="59">1 Jan 2017</text>
      <rect x="118" y="50" width="44" height="14" rx="2" fill="var(--navy)"/><text x="140" y="59">7 Feb 2017</text>
      <rect x="196" y="50" width="44" height="14" rx="2" fill="var(--navy)"/><text x="218" y="59">12 Mar 2017</text>
      <rect x="274" y="50" width="44" height="14" rx="2" fill="var(--navy)"/><text x="296" y="59">17 Apr 2017</text>
      <rect x="80" y="118" width="44" height="14" rx="2" fill="var(--navy)"/><text x="102" y="127">3 May 2017</text>
      <rect x="160" y="118" width="44" height="14" rx="2" fill="var(--navy)"/><text x="182" y="127">9 Jun 2017</text>
      <rect x="240" y="118" width="44" height="14" rx="2" fill="var(--navy)"/><text x="262" y="127">21 Jul 2017</text>
    </g>
    <g fill="var(--navy)"><circle cx="62" cy="78" r="2"/><circle cx="140" cy="78" r="2"/><circle cx="218" cy="78" r="2"/><circle cx="296" cy="78" r="2"/><circle cx="102" cy="108" r="2"/><circle cx="182" cy="108" r="2"/><circle cx="262" cy="108" r="2"/></g>
  </svg>
  <footer class="footer"><span class="brand"><span class="brand-mark"></span>Halden Grid Advisory</span><span>© 2017 Halden Grid Advisory. All rights reserved.</span><span>Page | 28</span></footer>
</section>

<!-- Row 11 -->
<section class="slide">
  <h2 class="slide-title">Process Chart #1</h2>
  <svg style="position:absolute;left:0;top:0" width="395" height="208" viewBox="0 0 395 208">
    <g fill="#fff" stroke="#ddd">
      <path d="M20 80 H58 L68 96 L58 112 H20 L30 96 Z"/><path d="M90 80 H128 L138 96 L128 112 H90 L100 96 Z"/><path d="M160 80 H198 L208 96 L198 112 H160 L170 96 Z"/><path d="M230 80 H268 L278 96 L268 112 H230 L240 96 Z"/><path d="M300 80 H338 L348 96 L338 112 H300 L310 96 Z"/>
    </g>
    <g font-size="4.5" fill="var(--navy)" text-anchor="middle"><text x="45" y="93">Lorem</text><text x="45" y="99">ipsum</text><text x="45" y="105">dolor sit</text>
      <text x="115" y="93">Lorem</text><text x="115" y="99">ipsum</text><text x="115" y="105">dolor sit</text>
      <text x="185" y="93">Lorem</text><text x="185" y="99">ipsum</text><text x="185" y="105">dolor sit</text>
      <text x="255" y="93">Lorem</text><text x="255" y="99">ipsum</text><text x="255" y="105">dolor sit</text>
      <text x="325" y="93">Lorem</text><text x="325" y="99">ipsum</text><text x="325" y="105">dolor sit</text></g>
    <g font-size="13" font-weight="700" fill="var(--gold)"><text x="72" y="101">1</text><text x="142" y="101">2</text><text x="212" y="101">3</text><text x="282" y="101">4</text><text x="352" y="101">5</text></g>
  </svg>
  <footer class="footer"><span class="brand"><span class="brand-mark"></span>Halden Grid Advisory</span><span>© 2017 Halden Grid Advisory. All rights reserved.</span><span>Page | 29</span></footer>
</section>

<section class="slide">
  <h2 class="slide-title">Process Chart #2</h2>
  <svg style="position:absolute;left:0;top:0" width="395" height="208" viewBox="0 0 395 208">
    <g fill="#fff" stroke="#ddd">
      <path d="M42 84 H80 L88 96 L80 108 H42 L50 96 Z"/><path d="M112 84 H150 L158 96 L150 108 H112 L120 96 Z"/><path d="M182 84 H220 L228 96 L220 108 H182 L190 96 Z"/><path d="M252 84 H290 L298 96 L290 108 H252 L260 96 Z"/><path d="M322 84 H360 L368 96 L360 108 H322 L330 96 Z"/>
    </g>
    <g fill="none" stroke="var(--gold)" stroke-width="1.5">
      <circle cx="32" cy="96" r="5"/><path d="M100 90 V102 M94 96 H106"/><path d="M164 91 L176 91 L170 101 Z"/><path d="M234 96 H246 M240 90 V102"/><circle cx="310" cy="96" r="5"/>
    </g>
    <g font-size="4.5" fill="var(--navy)" text-anchor="middle"><text x="66" y="95">Lorem ipsum</text><text x="66" y="101">dolor sit</text>
      <text x="136" y="95">Lorem ipsum</text><text x="136" y="101">dolor sit</text>
      <text x="206" y="95">Lorem ipsum</text><text x="206" y="101">dolor sit</text>
      <text x="276" y="95">Lorem ipsum</text><text x="276" y="101">dolor sit</text>
      <text x="346" y="95">Lorem ipsum</text><text x="346" y="101">dolor sit</text></g>
  </svg>
  <footer class="footer"><span class="brand"><span class="brand-mark"></span>Halden Grid Advisory</span><span>© 2017 Halden Grid Advisory. All rights reserved.</span><span>Page | 30</span></footer>
</section>

<section class="slide">
  <h2 class="slide-title">Process Chart #3</h2>
  <svg style="position:absolute;left:0;top:0" width="395" height="208" viewBox="0 0 395 208">
    <g fill="#fff" stroke="#ddd">
      <rect x="105" y="40" width="180" height="36"/><rect x="105" y="84" width="180" height="36"/><rect x="105" y="128" width="180" height="36"/>
    </g>
    <g fill="none" stroke="var(--gold)" stroke-width="1.3">
      <rect x="118" y="51" width="14" height="14" rx="2"/><circle cx="125" cy="102" r="7"/><path d="M118 153 L125 139 L132 153 Z"/>
    </g>
    <line x1="145" y1="44" x2="145" y2="72" stroke="#ddd"/><line x1="145" y1="88" x2="145" y2="116" stroke="#ddd"/><line x1="145" y1="132" x2="145" y2="160" stroke="#ddd"/>
    <g font-size="7" font-weight="700" fill="var(--navy)"><text x="152" y="61">Phase I</text><text x="152" y="105">Phase II</text><text x="152" y="149">Phase III</text></g>
    <g font-size="4.5" fill="var(--navy)"><text x="215" y="60">Lorem ipsum dolor sit</text><text x="215" y="104">Lorem ipsum dolor sit</text><text x="215" y="148">Lorem ipsum dolor sit</text></g>
  </svg>
  <footer class="footer"><span class="brand"><span class="brand-mark"></span>Halden Grid Advisory</span><span>© 2017 Halden Grid Advisory. All rights reserved.</span><span>Page | 31</span></footer>
</section>

<!-- Row 12 -->
<section class="slide">
  <h2 class="slide-title">5 Bullets Lists</h2>
  <svg style="position:absolute;left:0;top:0" width="395" height="208" viewBox="0 0 395 208">
    <circle cx="55" cy="72" r="13" fill="var(--navy)"/><circle cx="195" cy="72" r="13" fill="var(--red)"/><circle cx="335" cy="72" r="13" fill="var(--blue)"/>
    <circle cx="125" cy="125" r="13" fill="var(--gold)"/><circle cx="265" cy="125" r="13" fill="var(--green)"/>
    <g fill="none" stroke="#fff" stroke-width="1.3"><circle cx="55" cy="72" r="5"/><path d="M190 72 H200 M195 67 V77"/><rect x="330" y="67" width="10" height="10"/><path d="M120 129 L125 120 L130 129 Z"/><circle cx="265" cy="125" r="5"/></g>
    <g font-size="4.5" fill="#666"><text x="40" y="97">Lorem ipsum dolor sit</text><text x="212" y="74">Lorem ipsum dolor sit</text><text x="300" y="97">Lorem ipsum dolor sit</text><text x="110" y="150">Lorem ipsum dolor sit</text><text x="283" y="127">Lorem ipsum dolor sit</text></g>
  </svg>
  <footer class="footer"><span class="brand"><span class="brand-mark"></span>Halden Grid Advisory</span><span>© 2017 Halden Grid Advisory. All rights reserved.</span><span>Page | 32</span></footer>
</section>

<section class="slide">
  <h2 class="slide-title">Four Column chart</h2>
  <svg style="position:absolute;left:0;top:0" width="395" height="208" viewBox="0 0 395 208">
    <g font-size="4.3" fill="#fff" text-anchor="middle">
      <rect x="95" y="28" width="50" height="8" fill="var(--navy)"/><text x="120" y="33.5">Lorem Ipsum</text>
      <rect x="255" y="28" width="50" height="8" fill="var(--navy)"/><text x="280" y="33.5">Lorem Ipsum</text>
      <rect x="95" y="108" width="50" height="8" fill="var(--navy)"/><text x="120" y="113.5">Lorem Ipsum</text>
      <rect x="255" y="108" width="50" height="8" fill="var(--navy)"/><text x="280" y="113.5">Lorem Ipsum</text>
    </g>
    <line x1="60" y1="90" x2="180" y2="90" stroke="#ddd"/>
    <polyline points="65,65 95,58 125,60 170,52" fill="none" stroke="var(--red)" stroke-width="1.2"/>
    <polyline points="65,72 95,68 125,74 170,70" fill="none" stroke="var(--navy)" stroke-width="1.2"/>
    <polyline points="65,80 95,78 125,76 170,82" fill="none" stroke="var(--gold)" stroke-width="1.2"/>
    <line x1="220" y1="90" x2="340" y2="90" stroke="#ddd"/>
    <g fill="var(--navy)"><rect x="228" y="55" width="6" height="35"/><rect x="258" y="48" width="6" height="42"/><rect x="288" y="62" width="6" height="28"/><rect x="318" y="52" width="6" height="38"/></g>
    <g fill="var(--gold)"><rect x="235" y="65" width="6" height="25"/><rect x="265" y="60" width="6" height="30"/><rect x="295" y="70" width="6" height="20"/><rect x="325" y="66" width="6" height="24"/></g>
    <line x1="60" y1="175" x2="180" y2="175" stroke="#ddd"/>
    <g><rect x="68" y="135" width="8" height="40" fill="var(--navy)"/><rect x="68" y="125" width="8" height="10" fill="var(--gold)"/><rect x="68" y="120" width="8" height="5" fill="var(--red)"/>
      <rect x="98" y="140" width="8" height="35" fill="var(--navy)"/><rect x="98" y="130" width="8" height="10" fill="var(--gold)"/><rect x="98" y="124" width="8" height="6" fill="var(--red)"/>
      <rect x="128" y="138" width="8" height="37" fill="var(--navy)"/><rect x="128" y="128" width="8" height="10" fill="var(--gold)"/><rect x="128" y="122" width="8" height="6" fill="var(--red)"/>
      <rect x="158" y="142" width="8" height="33" fill="var(--navy)"/><rect x="158" y="132" width="8" height="10" fill="var(--gold)"/><rect x="158" y="126" width="8" height="6" fill="var(--red)"/></g>
    <path d="M220 175 L220 150 L250 140 L280 152 L310 135 L340 145 L340 175 Z" fill="var(--gold)"/>
    <path d="M220 175 L220 160 L250 155 L280 163 L310 150 L340 158 L340 175 Z" fill="var(--navy)"/>
  </svg>
  <footer class="footer"><span class="brand"><span class="brand-mark"></span>Halden Grid Advisory</span><span>© 2017 Halden Grid Advisory. All rights reserved.</span><span>Page | 33</span></footer>
</section>

<section class="slide">
  <div class="photo photo--towers-blue" role="img" aria-label="Transmission towers under cloudy sky in blue tint"></div>
  <div class="brand brand--sm" style="position:absolute;left:26px;top:22px"><span class="brand-mark"></span>Halden Grid Advisory</div>
  <h2 style="position:absolute;left:26px;top:116px;margin:0;color:#fff;font-size:18px;font-weight:400">THANK YOU</h2>
  <div style="position:absolute;left:26px;top:142px;color:var(--gold);font-size:5.5px;font-weight:700">Jon Anderson</div>
  <div style="position:absolute;left:26px;top:152px;color:#fff;font-size:5px;line-height:1.6">
    ☎ +1 415 555 0142<br>✉ info@kayseven.example<br>⌂ www.kayseven.example
  </div>
</section>

</main>
</body>
</html>
```